Ice Cream Container Print Design

This is an ice cream cup. This is for a homemade raspberry ice cream. I need it to be eye catching, pops from the shelf, with a gourmet look as well. I am looking for more of the Velmont Creme Ice cream type of style with it being elegant but also fun.

This goes into grocery shelves in the freezer. It has a clear lid so that is not included. The design sheet is for the space that wraps around the cup.

Target Market(s)

Grocery freezer shelves

Industry/Entity Type

Food Production

Font styles to use
Serif
Script

Colors
ec1f27
ffc214

Requirements
Must have
• Orvin's Logo and Fox Hollow. Please also use the berry cluster. I would like reds, golds, and blacks. I want a background design or color.
• I want it to say "Homemade Raspberry Ice Cream"
Nice to have
• As the spec sheet indicates on the bottom left, please make the front repeat 2 times as is goes around the cup.
Should not have
• Please do not make it look like a clown show. I want it fun and gourmet looking.

```html
<!DOCTYPE html>
<html lang="en">
<head>
<meta charset="utf-8">
<title>Orvin's Fox Hollow Homemade Raspberry Ice Cream – Cup Wrap</title>
<link href="https://fonts.googleapis.com/css2?family=Cormorant+Garamond:wght@600&family=Quicksand:wght@400&family=Dosis:wght@700&display=swap" rel="stylesheet">
<style>
  :root {
    --night: #120306;
    --glitter-deep: #2a1a08;
    --glitter-gold: #8a6a2a;
    --gold: #e8a92a;
    --cream: #f1e3c9;
    --cream-light: #fdf6ef;
    --peach: #f6d7b3;
    --cocoa: #6b4a1e;
    --berry-red: #c8192e;
    --scoop-pink: #ef9db3;
    --scoop-light: #f8cdd8;
    --berry-dark: #b3263f;
    --berry-light: #e0566f;
    --leaf: #4f8f2c;
  }
  * { margin: 0; padding: 0; box-sizing: border-box; }
  html, body { width: 1200px; height: 374px; overflow: hidden; background: var(--night); }
  .wrap { position: relative; width: 1200px; height: 374px; overflow: hidden; background: var(--night); }

  .glitter-top {
    position: absolute; left: 0; top: 0; width: 1200px; height: 90px;
    background: radial-gradient(ellipse at 50% 40%, var(--glitter-gold), var(--glitter-deep) 80%);
  }
  .night-band { position: absolute; left: 0; top: 0; width: 1200px; height: 160px; }

  .brand {
    position: absolute; top: 82px;
    font-family: "Cormorant Garamond", Georgia, serif; font-weight: 600;
    font-size: 44px; line-height: 1; color: var(--gold);
    transform: translateX(-50%); white-space: nowrap;
  }
  .brand--maker { left: 190px; }
  .brand--place { left: 718px; }

  .scoop {
    position: absolute; top: 92px; height: 68px;
    border-radius: 80px 80px 0 0 / 60px 60px 0 0;
    background: radial-gradient(ellipse at 40% 40%, var(--scoop-light), var(--scoop-pink) 75%);
  }
  .scoop--one { left: 334px; width: 160px; }
  .scoop--two { left: 954px; width: 152px; }

  .label-band { position: absolute; left: 0; top: 160px; width: 1200px; height: 108px; background: var(--cream); }
  .label-band .strip {
    position: absolute; left: 0; width: 1200px; height: 34px;
    background: var(--cream-light);
    border-bottom: 3px solid var(--peach);
  }
  .label-band .strip--upper { top: 10px; }
  .label-band .strip--lower { top: 54px; }

  .flavour { position: absolute; top: 160px; text-align: center; transform: translateX(-50%); white-space: nowrap; }
  .flavour--one { left: 206px; }
  .flavour--two { left: 814px; }
  .flavour .kind {
    display: block; font-family: "Quicksand", "Trebuchet MS", sans-serif; font-weight: 400;
    font-size: 33px; line-height: 44px; color: var(--cocoa);
  }
  .flavour .name {
    display: block; font-family: "Dosis", "Arial Narrow", sans-serif; font-weight: 700;
    font-size: 36px; line-height: 40px; letter-spacing: 2.5px; color: var(--berry-red);
  }

  .glitter-bottom {
    position: absolute; left: 0; top: 268px; width: 1200px; height: 106px;
    background: linear-gradient(180deg, var(--night) 0%, var(--glitter-deep) 55%, var(--glitter-gold) 100%);
  }
  .berries {
    position: absolute; top: 272px; height: 102px;
    border-radius: 120px 120px 0 0 / 70px 70px 0 0;
    background: radial-gradient(ellipse at 50% 100%, var(--berry-light), var(--berry-dark) 70%);
  }
  .berries--one { left: 190px; width: 322px; }
  .berries--two { left: 702px; width: 346px; }
</style>
</head>
<body>
<main class="wrap">
  <div class="glitter-top" role="img" aria-label="Gold glitter sparkle background"></div>

  <svg class="night-band" viewBox="0 0 1200 160" aria-hidden="true">
    <path d="M0 72 C200 56 420 58 600 56 C800 54 1000 62 1200 82 L1200 160 L0 160 Z" fill="var(--night)"/>
  </svg>

  <div class="brand brand--maker">Orvin's</div>
  <div class="brand brand--place">Fox Hollow</div>

  <div class="scoop scoop--one" role="img" aria-label="Scoop of pink raspberry ice cream"></div>
  <div class="scoop scoop--two" role="img" aria-label="Scoop of pink raspberry ice cream"></div>

  <div class="label-band">
    <div class="strip strip--upper"></div>
    <div class="strip strip--lower"></div>
  </div>

  <div class="flavour flavour--one">
    <span class="kind">homemade</span>
    <span class="name">RASPBERRY ICE CREAM</span>
  </div>
  <div class="flavour flavour--two">
    <span class="kind">homemade</span>
    <span class="name">RASPBERRY ICE CREAM</span>
  </div>

  <div class="glitter-bottom" role="img" aria-label="Gold bokeh glitter background"></div>
  <div class="berries berries--one" role="img" aria-label="Cluster of fresh raspberries with mint leaves"></div>
  <div class="berries berries--two" role="img" aria-label="Cluster of fresh raspberries with mint leaves"></div>
</main>
</body>
</html>
```